Letterhead to coordinate with business card

I am needing a docx template and print file for a letterhead to co-ordinate with my newly designed logo and business card.

```html
<!DOCTYPE html>
<html lang="en">
<head>
<meta charset="utf-8">
<title>Brightpath Plans – Letterhead</title>
<link href="https://fonts.googleapis.com/css2?family=Questrial&display=swap" rel="stylesheet">
<style>
  :root {
    --magenta: #a83067;
    --teal: #00827f;
    --ink: #444444;
    --ink-dark: #222222;
    --backdrop: #e2e2e2;
    --paper: #ffffff;
    --ghost: #f6f6f6;
  }
  * { margin: 0; padding: 0; box-sizing: border-box; }
  html, body {
    width: 1200px; height: 1200px; overflow: hidden;
    background: var(--backdrop);
    font-family: "Questrial", "Helvetica Neue", Arial, sans-serif;
  }
  .page {
    position: absolute; left: 204px; top: 40px;
    width: 792px; height: 1120px;
    background: var(--paper);
    color: var(--ink);
  }
  .brand {
    position: absolute; left: 520px; top: 70px; width: 200px;
    display: flex; flex-direction: column; align-items: center;
  }
  .brand-square { width: 72px; height: 72px; background: var(--magenta); }
  .brand-name {
    margin-top: 14px; font-size: 24px; color: var(--magenta);
    letter-spacing: 0.5px; white-space: nowrap;
  }
  .recipient {
    position: absolute; left: 71px; top: 249px;
    font-size: 14px; line-height: 21.4px;
  }
  .salutation {
    position: absolute; left: 71px; top: 398px; font-size: 14px;
  }
  .letter-body {
    position: absolute; left: 71px; top: 440px; width: 643px;
    font-size: 14px; line-height: 21.3px; text-align: justify;
  }
  .signature {
    position: absolute; left: 71px; top: 800px;
    width: 200px; height: 48px;
    background: linear-gradient(90deg, #e8e8e8, #f3f3f3);
  }
  .ghost-mark {
    position: absolute; left: 490px; top: 819px;
    width: 224px; height: 224px; background: var(--ghost);
  }
  .contact-band {
    position: absolute; left: 0; top: 1052px; width: 100%; height: 23px;
    background: var(--magenta); color: #fff;
    display: flex; align-items: center; justify-content: center; gap: 28px;
    font-size: 12.5px;
  }
  .contact-item { display: flex; align-items: center; gap: 3px; white-space: nowrap; }
  .contact-item svg { width: 9px; height: 9px; fill: var(--teal); }
  .web-address {
    position: absolute; left: 0; top: 1079px; width: 100%;
    text-align: center; font-size: 12.5px; color: var(--ink-dark);
  }
  .web-address strong { color: var(--magenta); font-weight: 400; }
</style>
</head>
<body>
  <main class="page">
    <header class="brand">
      <div class="brand-square"></div>
      <div class="brand-name">Brightpath Plans</div>
    </header>

    <address class="recipient" style="font-style:normal">
      Mr. Alan Marsh<br>
      President<br>
      Northgate Advisory<br>
      48 Harbour Road,<br>
      Lakeview State, 24001
    </address>

    <p class="salutation">Dear</p>

    <div class="letter-body">
      <p>Lorem ipsum dolor sit amet, consectetur adipiscing elit. Aenean ut ipsum eget massa hendrerit vestibulum vel in velit. Donec pretium neque velit.</p>
      <p>Aliquam porta lectus nec mauris ornare venenatis. Vivamus non est turpis, et cursus sem. Mauris vehicula erat in diam auctor at bibendum nisl lacinia.</p>
      <p>Morbi imperdiet neque vehicula nunc convallis gravida. Vestibulum iaculis pretium placerat. Integer consequat, est sit amet facilisis eleifend, nibh nibh varius orci, eget dapibus arcu dui non purus. Pellentesque in magna mauris. Duis enim sapien, dictum vitae condimentum a, pulvinar vel lacus. Mauris et molestie nibh. Vestibulum vitae nulla at metus elementum porta sit amet interdum elit. Nulla sollicitudin neque eu nulla volutpat congue.</p>
      <p>Etiam pellentesque, velit id dapibus fermentum, turpis sapien ornare dui, ac tincidunt ligula odio congue purus. Nunc sed ante dui, in porta lectus. Cras nec sem lorem. In hac habitasse platea dictumst. Maecenas id diam quis dui porta tristique. Sed id egestas felis. Donec ullamcorper mattis posuere. Phasellus fermentum eleifend tortor vel dapibus. Vestibulum ante ipsum.</p>
    </div>

    <div class="signature" role="img" aria-label="Handwritten signature of the sender"></div>

    <div class="ghost-mark" aria-hidden="true"></div>

    <footer>
      <div class="contact-band">
        <span class="contact-item">
          <svg viewBox="0 0 10 10"><path d="M5 0a3.5 3.5 0 0 0-3.5 3.5C1.5 6 5 10 5 10s3.5-4 3.5-6.5A3.5 3.5 0 0 0 5 0zm0 5a1.4 1.4 0 1 1 0-2.8A1.4 1.4 0 0 1 5 5z"/></svg>
          PO Box 204, Lakeview NSW 2400
        </span>
        <span class="contact-item">
          <svg viewBox="0 0 10 10"><path d="M2 0.5l2 2.2-1 1.2c.6 1.3 1.7 2.4 3 3l1.2-1 2.2 2-1.2 1.6C4.5 9.3.7 5.5.5 1.7z"/></svg>
          0400 123 987
        </span>
        <span class="contact-item">
          <svg viewBox="0 0 10 10"><path d="M0 2h10v6H0zm1 1v.3l4 2.5 4-2.5V3z"/></svg>
          info@brightpathplans.com.au
        </span>
      </div>
      <p class="web-address">www.<strong>brightpathplans</strong>.com</p>
    </footer>
  </main>
</body>
</html>
```